Evaporative Air Conditioning Summer Service

Would like to design a flyer to send out in an email to existing clients to promote a Pre-summer service for Evaporative Air Conditioners
Cost will be $110.00 inc gst
Tasks included in service are
- Inspection and clean of pads
- Inspection and check float valve, water pump, fan, motor, bearings, drain
- Clean basin
- Supply of bacterial tablet
- Inspect overall condition of unit
- Any repairs if required will be quoted
Please see files attached of a previous very basic flyer I have used for installation and replacement unit costs. This has current contact information
Have also uploaded company logo for use.
Thanks

```html
<!DOCTYPE html>
<html lang="en">
<head>
<meta charset="utf-8">
<title>Evaporative Air Conditioning Summer Service</title>
<link href="https://fonts.googleapis.com/css2?family=Arimo:wght@400;700&display=swap" rel="stylesheet">
<style>
  :root {
    --backdrop: #333333;
    --paper: #ffffff;
    --brand-blue: #2150aa;
    --accent-orange: #f07545;
    --ink: #333333;
    --sky-deep: #86a3d0;
    --sky-light: #b8cae3;
    --unit-grey: #c3c6cb;
    --unit-light: #dfe1e4;
  }
  * { margin: 0; padding: 0; box-sizing: border-box; }
  html, body { width: 1200px; height: 1200px; overflow: hidden; background: var(--backdrop); }
  body { font-family: "Arimo", Arial, sans-serif; position: relative; }

  .flyer {
    position: absolute; left: 250px; top: 106px;
    width: 700px; height: 990px;
    background: var(--paper); overflow: hidden;
  }

  .hero-photo {
    position: absolute; left: 0; top: 0; width: 700px; height: 440px;
    background:
      linear-gradient(180deg, #ffffff 0%, rgba(255,255,255,0) 15%, rgba(255,255,255,0) 74%, #ffffff 100%),
      linear-gradient(90deg, rgba(255,255,255,0.35) 0%, rgba(255,255,255,0) 30%, rgba(150,156,165,0.28) 62%, rgba(120,126,136,0.22) 85%, rgba(255,255,255,0.15) 100%),
      linear-gradient(180deg, var(--sky-light) 8%, var(--sky-deep) 26%, #a4badb 40%, var(--unit-light) 50%, var(--unit-grey) 66%, #b2b6bc 78%, #e4e5e7 90%);
  }

  .brand {
    position: absolute; left: 42px; top: 54px;
    display: flex; align-items: center; gap: 10px;
  }
  .brand-dot { width: 30px; height: 30px; border-radius: 50%; background: var(--brand-blue); }
  .brand-name { color: var(--brand-blue); font-weight: 700; font-size: 24px; letter-spacing: 0.5px; }

  .site-photo {
    position: absolute; left: 430px; top: 363px;
    width: 304px; height: 304px; border-radius: 50%;
    border: 10px solid var(--paper);
    background:
      linear-gradient(90deg, rgba(0,0,0,0.12) 0%, rgba(0,0,0,0) 20%, rgba(0,0,0,0) 80%, rgba(0,0,0,0.1) 100%),
      linear-gradient(180deg, #d6ccb7 0%, #e2dccf 24%, #f1efea 34%, #e8e6e2 46%, #4c5260 52%, #5d6370 66%, #7b808a 74%, #c9c6be 78%, #6c9a45 82%, #4f7d2f 100%);
    box-shadow: 0 0 12px rgba(0,0,0,0.08);
  }

  .headline {
    position: absolute; left: 66px; top: 430px;
    color: var(--brand-blue); font-weight: 700;
    font-size: 41.5px; line-height: 46.3px;
  }

  .offer { position: absolute; left: 66px; top: 604px; color: var(--ink); font-size: 18.7px; line-height: 21px; }
  .offer strong { font-weight: 700; }

  .task-list { position: absolute; left: 66px; top: 657px; list-style: none; color: var(--ink); font-size: 18.7px; line-height: 21.5px; }
  .task-list li { position: relative; padding-left: 25px; margin-bottom: 10px; width: 360px; }
  .task-list li svg { position: absolute; left: 2px; top: 6px; }

  .footer-waves { position: absolute; left: 0; top: 0; }

  .contact {
    position: absolute; right: 60px; top: 864px;
    text-align: right; color: var(--paper); font-size: 17.5px; line-height: 24px;
    font-style: normal;
  }
  .contact-title { font-weight: 700; font-size: 17.5px; }
</style>
</head>
<body>
  <main class="flyer">
    <div class="hero-photo" role="img" aria-label="Row of outdoor air conditioning condenser units on a rooftop under a blue sky"></div>

    <div class="brand">
      <span class="brand-dot"></span>
      <span class="brand-name">SUMMIT GAS &amp; PLUMBING</span>
    </div>

    <div class="site-photo" role="img" aria-label="Two air conditioning units beside a house wall on a lawn"></div>

    <h1 class="headline">Evaporative<br>Air Conditioning<br>Summer Service</h1>

    <p class="offer">Cost <strong>$110.00</strong> inc gst<br>Tasks included in service are</p>

    <ul class="task-list">
      <li><svg width="12" height="11" viewBox="0 0 12 11"><path d="M1 6 L4.5 9.5 L11 1" fill="none" stroke="#333" stroke-width="1.4"/></svg>Inspection and clean of pads</li>
      <li><svg width="12" height="11" viewBox="0 0 12 11"><path d="M1 6 L4.5 9.5 L11 1" fill="none" stroke="#333" stroke-width="1.4"/></svg>Inspection and check float valve, water pump, fan, motor, bearings, drain</li>
      <li><svg width="12" height="11" viewBox="0 0 12 11"><path d="M1 6 L4.5 9.5 L11 1" fill="none" stroke="#333" stroke-width="1.4"/></svg>Clean basin</li>
      <li><svg width="12" height="11" viewBox="0 0 12 11"><path d="M1 6 L4.5 9.5 L11 1" fill="none" stroke="#333" stroke-width="1.4"/></svg>Supply of bacterial tablet</li>
      <li><svg width="12" height="11" viewBox="0 0 12 11"><path d="M1 6 L4.5 9.5 L11 1" fill="none" stroke="#333" stroke-width="1.4"/></svg>Inspect overall condition of unit</li>
      <li><svg width="12" height="11" viewBox="0 0 12 11"><path d="M1 6 L4.5 9.5 L11 1" fill="none" stroke="#333" stroke-width="1.4"/></svg>Any repairs if required will be quoted</li>
    </ul>

    <svg class="footer-waves" width="700" height="990" viewBox="0 0 700 990" aria-hidden="true">
      <path d="M0 878 C 200 932, 450 880, 700 723 L700 990 L0 990 Z" fill="var(--accent-orange)"/>
      <path d="M0 900 C 200 952, 470 902, 700 751 L700 990 L0 990 Z" fill="var(--brand-blue)"/>
    </svg>

    <address class="contact">
      <div class="contact-title">Contact us</div>
      <div>0400555182</div>
      <div>admin@summitgasplumbing.com.au</div>
      <div>ABN 11222333444</div>
    </address>
  </main>
</body>
</html>
```